デパート等にてギフト商品として販売予定の商品になります。

1~2色でデザインして頂き、和風洋風は問いません。

下地色は 白、朱、紺、などの色からデザインして頂ければと思います。
・全体の3割~7割ほどが、透明で商品が見える設計にお願いします。
また、デザインに使用して頂くカラーは、 金、黒、白、朱、紺、などが基本色になりますので、通常こちらの色を使って下さい。

サイズ:120×220mm
オリジナリティ溢れるデザインを高く評価します。

具体的な採用イメージが定まっておりませんので、シンプルなデザインから繊細で豪華な感じまで、ご自由にデザインして頂ければと思います。
提案数が少なかったので、延長させていただきました。

別添のブランドロゴを使用する予定です。

既存のデザインに囚われない、感性の光ったご提案をお待ちしております。
細かい内容の追記となります。

「鯖の塩焼き」などの商品名は、人の手でシール貼付するため
縦長または横長よりも、正方形に近い形のほうが好ましいです。

この点、ご考慮いただけると幸いです。

シンプルで魅かれるデザイン

素晴らしいデザインに感激しております。

商品出来上がり後、もう一度、修正作業をご依頼させていただくと存じますが、
どうぞよろしくお願いいたします。

```html
<!DOCTYPE html>
<html lang="ja">
<head>
<meta charset="utf-8">
<title>ギフト商品パッケージデザイン 提案3</title>
<link href="https://fonts.googleapis.com/css2?family=Noto+Sans+JP:wght@400;500;700&family=Noto+Serif+JP:wght@500;700&display=swap" rel="stylesheet">
<style>
  :root {
    --paper: #ffffff;
    --ink: #2a2a2a;
    --vermilion: #b8262b;
    --black: #1c1a1a;
    --gold: #b08d57;
    --frame: #d8d8d8;
    --fish-light: #e4ddd0;
    --fish-mid: #b9ad9a;
    --fish-dark: #8c8272;
  }
  html, body {
    margin: 0;
    padding: 0;
    width: 857px;
    height: 1200px;
    overflow: hidden;
    background: var(--paper);
  }
  .sheet {
    position: relative;
    width: 857px;
    height: 1200px;
    font-family: "Noto Sans JP", sans-serif;
    color: var(--ink);
  }
  .sheet-title {
    position: absolute;
    left: 40px;
    top: 22px;
    margin: 0;
    font-size: 19px;
    font-weight: 500;
    letter-spacing: 0.04em;
  }
  .sheet-brand {
    position: absolute;
    left: 40px;
    top: 60px;
    margin: 0;
    font-size: 17px;
    font-weight: 500;
    letter-spacing: 0.08em;
  }
  .brand-mark {
    position: absolute;
    left: 60px;
    top: 150px;
    display: flex;
    align-items: center;
    gap: 12px;
    font-family: "Noto Sans JP", sans-serif;
    font-size: 30px;
    font-weight: 500;
    letter-spacing: 0.14em;
    color: var(--vermilion);
  }
  .brand-mark .dot {
    width: 20px;
    height: 20px;
    border-radius: 50%;
    background: var(--vermilion);
  }
  .scale-note {
    position: absolute;
    right: 40px;
    top: 340px;
    font-size: 17px;
  }
  .package {
    position: absolute;
    left: 14px;
    width: 829px;
    height: 356px;
    border: 2px solid var(--frame);
    box-sizing: border-box;
    overflow: hidden;
    background: var(--paper);
  }
  .package--red { top: 380px; }
  .package--black { top: 808px; }
  .package svg { display: block; }
  .product-label {
    position: absolute;
    left: 572px;
    top: 34px;
    width: 84px;
    height: 84px;
    display: flex;
    align-items: center;
    justify-content: center;
    text-align: center;
    font-family: "Noto Serif JP", serif;
    font-size: 18px;
    line-height: 1.35;
    color: #fff;
    background: var(--vermilion);
    opacity: 0.92;
  }
  .package--black .product-label { background: #9a2a2a; }
  .seal-name {
    position: absolute;
    left: 330px;
    top: 160px;
    width: 160px;
    text-align: center;
    font-size: 17px;
    font-weight: 500;
    letter-spacing: 0.16em;
  }
  .package--red .seal-name { color: #fff; }
  .package--black .seal-name { color: var(--gold); }
</style>
</head>
<body>
<main class="sheet">
  <h1 class="sheet-title">「お惣菜の詰合せ」ギフト商品のパッケージデザイン　提案３　2019.1.25</h1>
  <p class="sheet-brand">MINATO GOHAN</p>
  <div class="brand-mark"><span class="dot"></span>MINATO GOHAN</div>
  <div class="scale-note">90%表示</div>

  <section class="package package--red" aria-label="朱色版パッケージ">
    <svg width="825" height="352" viewBox="0 0 825 352">
      <defs>
        <linearGradient id="fishTone" x1="0" y1="0" x2="1" y2="1">
          <stop offset="0" stop-color="var(--fish-light)"/>
          <stop offset="0.5" stop-color="var(--fish-mid)"/>
          <stop offset="1" stop-color="var(--fish-dark)"/>
        </linearGradient>
      </defs>
      <rect x="100" y="0" width="630" height="352" fill="url(#fishTone)" role="img" aria-label="透明窓から見える鯖の塩焼き"/>
      <g fill="var(--vermilion)">
        <rect x="0" y="158" width="825" height="40"/>
        <circle cx="210" cy="178" r="44"/>
        <circle cx="295" cy="178" r="44"/>
        <circle cx="410" cy="178" r="100"/>
        <circle cx="525" cy="178" r="44"/>
        <circle cx="610" cy="178" r="44"/>
        <circle cx="695" cy="178" r="44"/>
        <circle cx="780" cy="178" r="44"/>
      </g>
      <circle cx="105" cy="178" r="48" fill="var(--paper)"/>
      <circle cx="105" cy="178" r="42" fill="var(--vermilion)" opacity="0.85" role="img" aria-label="和柄の丸紋"/>
    </svg>
    <div class="seal-name">MINATO GOHAN</div>
    <div class="product-label">鯖の<br>塩焼き</div>
  </section>

  <section class="package package--black" aria-label="黒色版パッケージ">
    <svg width="825" height="352" viewBox="0 0 825 352">
      <defs>
        <linearGradient id="fishTone2" x1="0" y1="0" x2="1" y2="1">
          <stop offset="0" stop-color="var(--fish-light)"/>
          <stop offset="0.5" stop-color="var(--fish-mid)"/>
          <stop offset="1" stop-color="var(--fish-dark)"/>
        </linearGradient>
      </defs>
      <rect x="100" y="0" width="630" height="352" fill="url(#fishTone2)" role="img" aria-label="透明窓から見える鯖の塩焼き"/>
      <g fill="var(--black)">
        <rect x="0" y="158" width="825" height="40"/>
        <circle cx="210" cy="178" r="44"/>
        <circle cx="295" cy="178" r="44"/>
        <circle cx="410" cy="178" r="100"/>
        <circle cx="525" cy="178" r="44"/>
        <circle cx="610" cy="178" r="44"/>
        <circle cx="695" cy="178" r="44"/>
        <circle cx="780" cy="178" r="44"/>
      </g>
      <circle cx="105" cy="178" r="48" fill="var(--paper)"/>
      <circle cx="105" cy="178" r="42" fill="var(--gold)" opacity="0.85" role="img" aria-label="金色の和柄の丸紋"/>
    </svg>
    <div class="seal-name">MINATO GOHAN</div>
    <div class="product-label">鯖の<br>塩焼き</div>
  </section>
</main>
</body>
</html>
```